Medical group practice

We need a flyer design incorporating the three doctors in the practice, there is a general practitioner, ophthalmologist and an obstetrician & Gynaecologist. see the attached file for the concept. will leave the colour design up to you

Target Market(s)

general public

Industry/Entity Type

Health Care

Colors

Designer to choose colors to be used in the design.

Requirements
Must have
• logos included in attachement

```html
<!DOCTYPE html>
<html lang="en">
<head>
<meta charset="utf-8">
<title>North Care Medical Centre – Open 7 Days</title>
<link rel="stylesheet" href="https://fonts.googleapis.com/css2?family=Bebas+Neue&family=Montserrat:wght@200;300;600;800&family=Source+Sans+3:wght@400;600&display=swap">
<style>
  :root {
    --orange: #eea71b;
    --orange-deep: #e9951a;
    --ink: #232323;
    --white: #ffffff;
    --paper: #f7f7f7;
    --text: #333333;
    --navy: #1f2f5c;
  }
  * { margin: 0; padding: 0; box-sizing: border-box; }
  html, body { width: 923px; height: 1200px; overflow: hidden; background: var(--white); }
  .flyer { position: relative; width: 923px; height: 1200px; overflow: hidden; background: var(--white); font-family: "Source Sans 3", sans-serif; color: var(--text); }

  .top-band { position: absolute; left: 0; top: 0; width: 923px; height: 340px; background: linear-gradient(180deg, var(--orange) 0%, var(--orange-deep) 100%); }

  .doctor-photo { position: absolute; left: 0; top: 543px; width: 923px; height: 393px;
    background: linear-gradient(90deg, #dfe3e6 0%, #eef0f1 40%, #e6e8ea 70%, #c9ccd0 100%); }

  .hours-panel { position: absolute; left: 0; top: 0; width: 923px; height: 600px; }
  .hours-text { position: absolute; left: 0; top: 110px; width: 316px; text-align: center;
    font-family: "Bebas Neue", sans-serif; color: var(--white); font-size: 156px; line-height: 1; }
  .hours-text span { display: block; height: 156px; }

  .brand { position: absolute; right: 56px; top: 48px; text-align: right; color: var(--white); font-family: "Montserrat", sans-serif; }
  .brand-first { font-weight: 200; font-size: 76px; line-height: 72px; }
  .brand-main { font-weight: 800; font-size: 70px; line-height: 66px; }
  .brand-sub { font-weight: 200; font-size: 43px; line-height: 46px; }
  .brand-rule { position: absolute; left: 478px; top: 227px; width: 389px; height: 4px; background: var(--white); }
  .tagline { position: absolute; right: 56px; top: 268px; width: 420px; text-align: right; color: var(--white); font-size: 15.5px; line-height: 22px; }

  .billing { font-family: "Montserrat", sans-serif; font-weight: 600; font-size: 34px; letter-spacing: 20px; color: var(--white); }
  .billing div { position: absolute; left: 385px; padding-left: 8px; display: flex; align-items: center; }
  .billing-bulk { top: 376px; width: 276px; height: 39px; background: var(--orange); }
  .billing-mid { top: 415px; width: 492px; height: 49px; background: var(--ink); }
  .billing-gap { top: 466px; width: 387px; height: 38px; background: var(--orange); }

  .practitioners { position: absolute; left: 0; top: 936px; width: 923px; height: 236px; background: var(--paper); }
  .practice { position: absolute; top: 14px; text-align: center; }
  .practice-mark { display: flex; align-items: center; justify-content: center; gap: 6px; height: 52px; font-weight: 600; font-size: 13px; color: var(--navy); }
  .practice-mark i { display: block; width: 14px; height: 14px; border-radius: 50%; background: var(--navy); }
  .practice-name { font-weight: 600; font-size: 16px; line-height: 19px; color: #111; }
  .practice-role { font-size: 14.5px; line-height: 19px; }
  .practice-list { font-size: 9.5px; line-height: 13px; }

  .practice-obgyn { left: 10px; width: 340px; }
  .practice-gp { left: 330px; width: 290px; }
  .practice-eye { left: 610px; width: 310px; }
  .practice-gp .practice-name { font-size: 18px; line-height: 20px; }
  .obgyn-detail { text-align: left; margin-top: 8px; }
  .obgyn-detail p { margin-bottom: 6px; }

  .bottom-band { position: absolute; left: 0; top: 1172px; width: 923px; height: 28px; background: var(--orange-deep); }
</style>
</head>
<body>
<main class="flyer">
  <div class="top-band"></div>

  <div class="doctor-photo" role="img" aria-label="Smiling doctor in white coat with stethoscope standing in a bright clinic room"></div>

  <svg class="hours-panel" viewBox="0 0 923 600" aria-hidden="true">
    <polygon points="0,105 447,105 333,575 0,575" fill="#232323"/>
  </svg>
  <h2 class="hours-text"><span>Open</span><span>7</span><span>Days</span></h2>

  <header class="brand">
    <div class="brand-first">NORTH</div>
    <div class="brand-main">CARE</div>
    <div class="brand-sub">MEDICAL CENTRE</div>
  </header>
  <div class="brand-rule"></div>
  <p class="tagline">Dolorem ipsum quia dolor sit amet teturadipisci<br>velitsed quia non mquam eius m i tempora</p>

  <div class="billing">
    <div class="billing-bulk">BULK</div>
    <div class="billing-mid">BILLING</div>
    <div class="billing-gap">NO GAP</div>
  </div>

  <section class="practitioners">
    <article class="practice practice-obgyn">
      <div class="practice-mark"><i></i>Mehta Women's Health</div>
      <div class="practice-name">Dr. Arjun Mehta, BMedSci, MBBS,<br>DM (O&amp;G), FACOG</div>
      <div class="practice-role">Obstetrician &amp; Gynaecologist<br>Email: drmehta@example.com</div>
      <div class="practice-list obgyn-detail">
        <p>Obstetrics:&nbsp;&nbsp;&nbsp;&nbsp;Prenatal Care, Delivery, Postnatal checks, High Risk pregnancy</p>
        <p style="text-align:center">Gynaecology : Pap smears, Abnormal vaginal bleeding, Fibroids, Colposcopy,<br>Family planning, Infertility, Cancer screening, And More….</p>
      </div>
    </article>

    <article class="practice practice-gp">
      <div class="practice-mark"><i></i>Barrett Family Practice</div>
      <div class="practice-name">Dr. Colin Barrett, MD.</div>
      <div class="practice-list">General Practitioner<br>colin.barrett.doc@example.com</div>
      <div class="practice-list" style="margin-top:10px">General Checks<br>Annual Check ups<br>Wound Care/Dressings<br>Incision &amp; Drainage<br>Suturing lacerations<br>Pain Injections<br>Glucose checks<br>Foreign Body Removal</div>
    </article>

    <article class="practice practice-eye">
      <div class="practice-mark"><i></i>Clearview</div>
      <div class="practice-name">Clearview Eye Care<br>Dr. Lucia R. Fernandez</div>
      <div class="practice-role">MD. Surgeon Ophthalmologist<br>Email: lucia.eyes@example.com<br>Eyes disease examination,<br>Surgery of Pterygium, Cataract,<br>Glaucoma, Emergency: Conjunctivitis,<br>Traumatism, Foreign body and more</div>
    </article>
  </section>

  <div class="bottom-band"></div>
</main>
</body>
</html>
```